UK landscaping company needs website

We, Brindle Landscapes need a website design for a company based in Surrey, UK. The design should be bold and playful. We have three main areas of work driveways, paving and fencing. It shouldn't be too heavy in text and concentrate on the pictures from previous jobs we've completed. You may use stock images for the design, these can be changed if you are successful. Please don’t just copy the flyer it is just there to provide content.
We have a logo design which we would also like editing slightly.
Here are some of my local competitors
https://www.vexmoorlandscapes.co.uk/

https://www.twinreedgardendesign.com/

https://quarnelllandscapes.co.uk/

Industry/Entity Type

Landscaping

Coding

Coded - Design and coding required

Number of Pages Required

3 page

Font styles to use
Sans Serif

Requirements
Must have
• Pictures of my previous jobs.
Must be mobile friendly
Easy to navigate
Nice to have
• Try to use different colours. It would be good to have some designs that aren’t just black and green.
I’d like some curves in the design.
Should not have
• We install hard landscaping. Think more building/construction and less plants and cutting grass.

```html
<!DOCTYPE html>
<html lang="en">
<head>
<meta charset="utf-8">
<title>Brindle Landscapes</title>
<link rel="stylesheet" href="https://fonts.googleapis.com/css2?family=Montserrat:ital,wght@0,400;0,500;0,600;0,700;1,400&display=swap">
<style>
:root{
  --green:#72bf44;
  --green-dark:#5ea534;
  --yellow:#f5cc00;
  --ink:#2a2c3d;
  --text:#4a4a4a;
  --muted:#8a8a95;
  --pale:#f2f3f8;
  --footer:#2c2f43;
  --white:#fff;
}
*{box-sizing:border-box;margin:0;padding:0}
html,body{width:1200px;height:4081px;overflow:hidden}
body{position:relative;font-family:"Montserrat",sans-serif;color:var(--text);background:var(--white)}
.abs{position:absolute}
a{color:inherit;text-decoration:none}
.brand{font-weight:700;color:var(--ink);font-size:30px;letter-spacing:-1px;display:flex;align-items:center;gap:8px}
.brand .dot{width:14px;height:14px;border-radius:50%;background:var(--green)}
.mark{position:relative;display:inline-block}
.mark::before{content:"";position:absolute;left:-12px;top:-6px;width:30px;height:30px;border-radius:50%;background:var(--green);z-index:-1}
.mark.y::before{background:var(--yellow)}
.btn{display:flex;align-items:center;justify-content:center;background:var(--green);color:#fff;font-weight:600;border-radius:40px;text-transform:uppercase}
.btn-wrap{position:absolute}
.btn-wrap .ball{position:absolute;border-radius:50%;background:var(--yellow);opacity:.95}

/* top */
.topline{left:0;top:0;width:1200px;height:4px;background:linear-gradient(90deg,var(--green) 0 50%,var(--yellow) 50%)}
.hero-photo{left:440px;top:0;width:760px;height:676px;background:linear-gradient(180deg,#b8c9d9 0%,#cdd6da 35%,#8d7560 50%,#b49a72 62%,#c9bfae 80%,#d8d3c8 100%)}
.hero-fade{left:0;top:0;width:1200px;height:676px;background:linear-gradient(90deg,#fff 0 38%,rgba(255,255,255,.85) 50%,rgba(255,255,255,0) 72%)}
.nav{top:58px;left:639px;display:flex;gap:34px;font-size:13px;color:var(--ink);font-weight:500}
.nav .home{position:relative}
.nav .home::before{content:"";position:absolute;left:-4px;top:-3px;width:9px;height:9px;border-radius:50%;background:var(--yellow)}
.call{left:1003px;top:48px}
.call small{display:block;color:var(--yellow);font-size:9px;font-weight:500}
.call b{display:block;color:var(--ink);font-size:15px;font-weight:500}
.call-icon{left:954px;top:30px}
.hero-kicker{left:135px;top:262px;color:var(--green);font-size:17px;font-weight:500}
.hero-title{left:130px;top:282px;color:var(--ink);font-size:68px;font-weight:600;letter-spacing:1px}
.hero-text{left:135px;top:374px;width:475px;font-size:16px;line-height:25px;color:var(--ink)}
.slider{left:560px;top:598px;width:80px;height:36px;border-radius:18px;background:var(--green);display:flex;align-items:center;justify-content:center;gap:12px}

/* about */
.arc-left{left:-220px;top:680px}
.tile{position:absolute}
.tile .back{position:absolute}
.tile .ph{position:absolute;inset:0;border:4px solid #fff;box-shadow:0 6px 18px rgba(0,0,0,.12)}
.about-title{left:602px;top:920px;font-size:32px;font-weight:500;color:var(--ink);display:flex;gap:14px;align-items:baseline}
.about-title .brand{font-size:24px}
.about-text{left:608px;top:984px;width:440px;font-size:13px;line-height:19px;color:var(--ink)}
.about-text p+p{margin-top:18px}

/* services */
.services{left:0;top:1481px;width:1200px;height:986px;background:var(--pale);overflow:hidden}
.sec-title{width:1200px;left:0;text-align:center;font-size:32px;font-weight:500;color:var(--ink)}
.sec-sub{width:1200px;left:0;text-align:center;font-size:12px;line-height:19px;color:var(--muted)}
.card{position:absolute;width:263px;height:260px;background:#fff;border-bottom:4px solid var(--yellow);display:flex;flex-direction:column;align-items:center;text-align:center;color:var(--ink)}
.card.active{background:var(--green);color:#fff;border-bottom-color:var(--green)}
.card svg.ic{margin-top:84px;height:56px}
.card h3{font-size:18px;font-weight:500;margin-top:12px}
.card .arrow{margin-top:24px}
.grass{left:0;top:2282px;width:1200px;height:185px;background:linear-gradient(180deg,rgba(255,255,255,0) 0%,#9fd85a 45%,#4f9a20 100%)}

/* testimonials */
.t-col{position:absolute;width:290px;text-align:center;color:var(--ink)}
.t-card{position:absolute;left:456px;top:2758px;width:287px;height:242px;background:#fff;box-shadow:0 6px 26px rgba(0,0,0,.08)}
.avatar{width:66px;height:66px;border-radius:50%;margin:0 auto;background:linear-gradient(135deg,#c9a48a,#8b5e46);border:3px solid #fff;box-shadow:0 3px 10px rgba(0,0,0,.15)}
.t-col h4{font-size:16px;font-weight:600;margin-top:14px}
.t-col .co{font-size:10px;font-style:italic;color:#c0c0c8;margin-top:4px}
.t-col p{font-size:12px;line-height:19px;margin:20px auto 0;width:220px}
.stars{margin-top:14px;color:var(--yellow);font-size:15px;letter-spacing:5px}

/* gallery */
.g{position:absolute;overflow:hidden}
.g .cap{position:absolute;left:26px;bottom:24px;color:#fff;font-size:18px;font-weight:500;z-index:2}
.g .plus{position:absolute;right:20px;bottom:20px;width:22px;height:22px;background:#fff;z-index:2;display:flex;align-items:center;justify-content:center;color:var(--ink);font-weight:700;font-size:18px;line-height:1}
.g .shade{position:absolute;left:0;right:0;bottom:0;height:45%;background:linear-gradient(180deg,rgba(0,0,0,0),rgba(0,0,0,.75));z-index:1}
.promo{left:957px;top:3405px;width:243px;height:252px;background:var(--green);color:#fff;text-align:center}
.promo .brand{color:#fff;justify-content:center;margin-top:40px;font-size:26px}
.promo p{font-size:11px;line-height:15px;margin:30px auto 0;width:200px;font-weight:500}

/* footer */
.footer{left:0;top:3657px;width:1200px;height:424px;background:var(--footer);overflow:hidden;color:#fff}
.f-brand{left:146px;top:125px}
.f-brand .brand{color:#fff}
.f-contact{left:146px;top:188px;font-size:13px}
.f-contact li{list-style:none;display:flex;align-items:center;gap:10px;height:32px}
.ico-c{width:22px;height:22px;border-radius:50%;background:var(--green);display:inline-flex;align-items:center;justify-content:center}
.social{left:146px;top:272px;display:flex;gap:8px}
.social span{width:28px;height:28px;border-radius:50%}
.f-col{position:absolute;top:150px}
.f-col h5{font-size:15px;font-weight:500;position:relative;margin-bottom:14px}
.f-col h5::before{content:"";position:absolute;left:-14px;top:-6px;width:22px;height:22px;border-radius:50%;background:var(--green);z-index:0}
.f-col h5.y::before{background:var(--yellow)}
.f-col h5 span{position:relative}
.f-col a{display:block;font-size:13px;color:#9ea3c0;height:31px}
.vline{width:1px;height:95px;background:#44485f;top:178px}
.hline{left:146px;top:353px;width:908px;height:1px;background:#44485f}
.copy{left:0;top:386px;width:1200px;text-align:center;font-size:14px;font-weight:500}
.copy span{color:var(--yellow)}
</style>
</head>
<body>

<!-- HERO -->
<header>
  <div class="abs hero-photo" role="img" aria-label="Photo of a stone-clad bungalow with a wide garage and a fresh gravel driveway"></div>
  <div class="abs hero-fade"></div>
  <div class="abs topline"></div>
  <div class="abs" style="left:130px;top:36px"><span class="brand">BRINDLE<span class="dot"></span></span></div>
  <nav class="abs nav">
    <a class="home" href="#">Home</a><a href="#">About</a><a href="#">Services</a><a href="#">Gallery</a>
  </nav>
  <svg class="abs call-icon" width="44" height="50" viewBox="0 0 44 50">
    <circle cx="17" cy="18" r="17" fill="var(--yellow)"/>
    <circle cx="24" cy="28" r="16" fill="var(--green)" opacity=".9"/>
    <path d="M31 40c-6 0-12-6-12-12l3-2 3 4-2 2c1 2 2 3 4 4l2-2 4 3z" fill="var(--ink)"/>
  </svg>
  <div class="abs call"><small>Call for free estimate</small><b>07700 900 418</b></div>

  <div class="abs hero-kicker">Welcome to Brindle Landscapes</div>
  <h1 class="abs hero-title">Driveways</h1>
  <p class="abs hero-text">We at Brindle Landscapes are a professional, experienced landscaping business that delivers premium garden</p>
  <div class="btn-wrap" style="left:128px;top:452px">
    <span class="ball" style="left:0;top:0;width:44px;height:44px"></span>
    <a class="btn" href="#" style="position:absolute;left:12px;top:12px;width:299px;height:59px;font-size:15px">Call for a free estimate</a>
  </div>
  <div class="abs slider">
    <svg width="14" height="12" viewBox="0 0 14 12"><path d="M7 1 2 6l5 5M2 6h11" stroke="#fff" stroke-width="2" fill="none"/></svg>
    <svg width="14" height="12" viewBox="0 0 14 12"><path d="M7 1l5 5-5 5M12 6H1" stroke="#fff" stroke-width="2" fill="none"/></svg>
  </div>
</header>

<!-- ABOUT -->
<section>
  <svg class="abs arc-left" width="360" height="440" viewBox="0 0 360 440">
    <circle cx="110" cy="220" r="210" fill="none" stroke="var(--green)" stroke-width="9"/>
  </svg>
  <svg class="abs" style="left:210px;top:1230px" width="150" height="150" viewBox="0 0 150 150">
    <circle cx="75" cy="75" r="63" fill="none" stroke="var(--yellow)" stroke-width="9"/>
  </svg>

  <div class="tile" style="left:81px;top:797px;width:203px;height:195px">
    <div class="back" style="left:-4px;top:-12px;width:210px;height:200px;background:var(--green);transform:rotate(-2deg)"></div>
    <div class="ph" role="img" aria-label="Timber pergola over a pale stone patio" style="background:linear-gradient(160deg,#7a5a44,#9b8670 45%,#d7d4cf)"></div>
  </div>
  <div class="tile" style="left:301px;top:818px;width:203px;height:288px">
    <div class="back" style="left:6px;top:4px;width:210px;height:292px;background:var(--yellow);transform:rotate(2deg)"></div>
    <div class="ph" role="img" aria-label="New lawn edged by sleeper retaining wall beside timber decking" style="background:linear-gradient(175deg,#c9a66b 0 28%,#3e6b2a 40%,#4f7f33 70%,#a47e52)"></div>
  </div>
  <div class="tile" style="left:81px;top:1016px;width:203px;height:288px">
    <div class="back" style="left:-14px;top:10px;width:210px;height:290px;background:var(--yellow);transform:rotate(-2deg)"></div>
    <div class="ph" role="img" aria-label="Circular sandstone paving patio in front of a grey summerhouse" style="background:linear-gradient(180deg,#8c9097 0 35%,#c8aa98 45%,#d6b8a6)"></div>
  </div>
  <div class="tile" style="left:301px;top:1130px;width:203px;height:195px">
    <div class="back" style="left:8px;top:10px;width:210px;height:200px;background:var(--green);transform:rotate(2deg)"></div>
    <div class="ph" role="img" aria-label="Dark block paved path with curved step" style="background:linear-gradient(160deg,#c9c9c9,#5d5e62 45%,#3c3e43)"></div>
  </div>

  <h2 class="abs about-title"><span class="mark">About</span><span class="brand">BRINDLE<span class="dot"></span></span></h2>
  <div class="abs about-text">
    <p>We at Brindle Landscapes are a professional, experienced landscaping business that delivers premium garden construction at an affordable price. We provide all aspects of hard and soft landscaping throughout Surrey and surrounding areas.</p>
    <p>We pride ourselves on excellent workmanship and attention to detail. Using only top quality materials to ensure an outstanding and long-lasting finish, installed using both traditional and modern techniques.</p>
  </div>
  <div class="btn-wrap" style="left:598px;top:1180px">
    <span class="ball" style="left:0;top:0;width:32px;height:32px"></span>
    <a class="btn" href="#" style="position:absolute;left:9px;top:13px;width:225px;height:43px;font-size:11px">Call for a free estimate</a>
  </div>
</section>

<!-- SERVICES -->
<section class="abs services">
  <svg class="abs" style="left:980px;top:85px" width="260" height="430" viewBox="0 0 260 430">
    <circle cx="230" cy="215" r="205" fill="none" stroke="var(--green)" stroke-width="9"/>
  </svg>
  <svg class="abs" style="left:-40px;top:640px" width="360" height="360" viewBox="0 0 360 360">
    <circle cx="150" cy="190" r="185" fill="var(--yellow)"/>
  </svg>
  <h2 class="abs sec-title" style="top:100px"><span class="mark y">Services we provide</span></h2>
  <p class="abs sec-sub" style="top:152px">It is a long established fact that a reader will be distracted by the readable<br>content of a page when looking at its layout.</p>

  <div class="card" style="left:187px;top:240px">
    <svg class="ic" viewBox="0 0 80 56" width="80"><path d="M40 2l14 14-14 14-14-14z" fill="var(--ink)"/><path d="M22 20l14 14-14 14L8 34z" fill="var(--green)"/><path d="M58 20l14 14-14 14-14-14z" fill="var(--green)"/><path d="M40 38l9 9-9 9-9-9z" fill="var(--ink)"/></svg>
    <h3>Driveways</h3>
    <svg class="arrow" width="28" height="12" viewBox="0 0 28 12"><path d="M0 6h26M21 1l5 5-5 5" stroke="#c4c4cc" stroke-width="1.6" fill="none"/></svg>
  </div>
  <div class="card active" style="left:469px;top:240px">
    <svg class="ic" viewBox="0 0 70 56" width="70"><g stroke="#fff" stroke-width="4" fill="none"><path d="M6 52h58M6 42h58"/><path d="M20 40V24M35 40V6M50 40V20"/><path d="M20 30l-7-5M20 30l7-5M35 18l-7-5M35 18l7-5M35 28l-7-5M35 28l7-5M50 30l-7-5M50 30l7-5"/></g></svg>
    <h3>Garden Design</h3>
    <svg class="arrow" width="28" height="12" viewBox="0 0 28 12"><path d="M0 6h26M21 1l5 5-5 5" stroke="#fff" stroke-width="2" fill="none"/></svg>
  </div>
  <div class="card" style="left:750px;top:240px">
    <svg class="ic" viewBox="0 0 80 56" width="80"><path d="M40 0l14 14-14 14-14-14z" fill="var(--green)"/><path d="M22 18l14 14-14 14L8 32z" fill="var(--ink)"/><path d="M58 18l14 14-14 14-14-14z" fill="var(--ink)"/><path d="M40 36l10 10-10 10-10-10z" fill="var(--green)"/></svg>
    <h3>Paving &amp; Brickwork</h3>
    <svg class="arrow" width="28" height="12" viewBox="0 0 28 12"><path d="M0 6h26M21 1l5 5-5 5" stroke="#c4c4cc" stroke-width="1.6" fill="none"/></svg>
  </div>
  <div class="card" style="left:187px;top:520px">
    <svg class="ic" viewBox="0 0 60 56" width="60"><path d="M30 34V18" stroke="var(--ink)" stroke-width="4"/><path d="M30 20c-2-10-12-12-18-10 2 8 10 12 18 10zM30 18c2-10 12-12 18-10-2 8-10 12-18 10z" fill="var(--green)"/><path d="M4 56c4-14 14-20 26-20s22 6 26 20z" fill="var(--ink)"/></svg>
    <h3>Planting &amp; Turfing</h3>
    <svg class="arrow" width="28" height="12" viewBox="0 0 28 12"><path d="M0 6h26M21 1l5 5-5 5" stroke="#c4c4cc" stroke-width="1.6" fill="none"/></svg>
  </div>
  <div class="card" style="left:469px;top:520px">
    <svg class="ic" viewBox="0 0 64 56" width="64"><g fill="var(--ink)"><path d="M4 8l6-6 6 6v48H4zM20 8l6-6 6 6v48H20zM36 8l6-6 6 6v48H36zM52 8l6-6 6 6v48H52z"/></g><rect x="0" y="16" width="64" height="8" fill="var(--green)"/><rect x="0" y="36" width="64" height="8" fill="var(--green)"/></svg>
    <h3>Fencing &amp; Decking</h3>
    <svg class="arrow" width="28" height="12" viewBox="0 0 28 12"><path d="M0 6h26M21 1l5 5-5 5" stroke="#c4c4cc" stroke-width="1.6" fill="none"/></svg>
  </div>
  <div class="card" style="left:750px;top:520px">
    <svg class="ic" viewBox="0 0 64 56" width="64"><path d="M6 56c0-20 2-30 10-38-2 14 0 26 4 38z" fill="var(--ink)"/><path d="M18 56c-2-24 0-40 10-54-2 20 0 38 6 54z" fill="var(--green)"/><path d="M32 56c2-18 8-28 18-34-6 12-8 22-8 34z" fill="var(--ink)"/><path d="M46 56c0-14 6-24 16-30-4 10-6 20-6 30z" fill="var(--green)"/></svg>
    <h3>Artificial Grass</h3>
    <svg class="arrow" width="28" height="12" viewBox="0 0 28 12"><path d="M0 6h26M21 1l5 5-5 5" stroke="#c4c4cc" stroke-width="1.6" fill="none"/></svg>
  </div>
</section>
<div class="abs grass" role="img" aria-label="Band of tall green grass blades along the section edge"></div>

<!-- TESTIMONIALS -->
<section>
  <svg class="abs" style="left:1025px;top:2960px" width="175" height="183" viewBox="0 0 175 183">
    <circle cx="150" cy="160" r="150" fill="var(--green)"/>
  </svg>
  <h2 class="abs sec-title" style="top:2590px"><span class="mark">Testimonials</span></h2>
  <p class="abs sec-sub" style="top:2635px">Lorem ipsum is simply dummy text of the printing and typesetting</p>

  <div class="t-card"></div>
  <svg class="abs" style="left:412px;top:2950px" width="100" height="100" viewBox="0 0 100 100">
    <circle cx="50" cy="50" r="40" fill="none" stroke="var(--yellow)" stroke-width="8"/>
  </svg>

  <div class="t-col" style="left:166px;top:2728px">
    <div class="avatar" role="img" aria-label="Customer portrait"></div>
    <h4>Nora Whitfield</h4><div class="co">Fernway Ltd</div>
    <p>It is a long established fact that a reader will be distracted by the readable content of a page when</p>
    <div class="stars">★★★☆☆</div>
  </div>
  <div class="t-col" style="left:454px;top:2728px">
    <div class="avatar" role="img" aria-label="Customer portrait" style="background:linear-gradient(135deg,#f3a6b8,#7a4a3a)"></div>
    <h4>Teodor Brandt</h4><div class="co">Head of Operations, Calder</div>
    <p>It is a long established fact that a reader will be distracted by the readable content of a page when</p>
    <div class="stars">★★★★★</div>
  </div>
  <div class="t-col" style="left:746px;top:2728px">
    <div class="avatar" role="img" aria-label="Customer portrait" style="background:linear-gradient(135deg,#e8e4e0,#a07860)"></div>
    <h4>Nora Whitfield</h4><div class="co">Fernway Ltd</div>
    <p>It is a long established fact that a reader will be distracted by the readable content of a page when</p>
    <div class="stars">★★★☆☆</div>
  </div>
</section>

<!-- GALLERY -->
<section>
  <div class="g" style="left:0;top:3143px;width:544px;height:514px">
    <div style="position:absolute;inset:0;background:linear-gradient(180deg,#8fb36a 0 18%,#8a5a44 30%,#9c7a58 45%,#b08a60 60%,#5f9a35 80%,#4e8a2c)" role="img" aria-label="Tall timber fence and new lawn in front of a brick house"></div>
    <div class="shade"></div><span class="cap">Image Name</span><span class="plus">+</span>
  </div>
  <div class="g" style="left:544px;top:3143px;width:328px;height:262px">
    <div style="position:absolute;inset:0;background:linear-gradient(170deg,#e7e2d6 0 20%,#b59a6c 40%,#6d6358 65%,#4b4a4c)" role="img" aria-label="Timber pergola over a grey patio"></div>
    <div class="shade"></div><span class="cap">Image Name</span><span class="plus">+</span>
  </div>
  <div class="g" style="left:872px;top:3143px;width:328px;height:262px">
    <div style="position:absolute;inset:0;background:linear-gradient(170deg,#dfe2e6 0 15%,#c9a16e 35%,#c9c1b0 55%,#6d9a48 75%,#4f7c32)" role="img" aria-label="Fenced garden with lawn and raised planters"></div>
    <div class="shade"></div><span class="cap">Image Name</span><span class="plus">+</span>
  </div>
  <div class="g" style="left:544px;top:3405px;width:413px;height:252px">
    <div style="position:absolute;inset:0;background:linear-gradient(150deg,#8a4f3c 0 20%,#5f9c3a 38%,#b7b3ab 60%,#8e8a84)" role="img" aria-label="Brick walled garden with lawn and paved steps"></div>
    <div class="shade"></div><span class="cap">Image Name</span><span class="plus">+</span>
  </div>
  <div class="abs promo">
    <div class="brand">BRINDLE<span class="dot" style="background:#fff"></span></div>
    <p>Book with us directly and get the best available rate</p>
    <div class="btn-wrap" style="left:45px;top:170px">
      <span class="ball" style="left:0;top:0;width:26px;height:26px"></span>
      <a class="btn" href="#" style="position:absolute;left:13px;top:8px;width:125px;height:32px;font-size:10px;background:#fff;color:var(--green)">View more</a>
    </div>
  </div>
</section>

<!-- FOOTER -->
<footer class="abs footer">
  <svg class="abs" style="left:-60px;top:-20px" width="260" height="260" viewBox="0 0 260 260">
    <path d="M140 0A190 190 0 0 1 0 240" fill="none" stroke="var(--green)" stroke-width="8"/>
  </svg>
  <svg class="abs" style="left:1060px;top:290px" width="140" height="134" viewBox="0 0 140 134">
    <circle cx="150" cy="150" r="140" fill="var(--yellow)"/>
  </svg>
  <div class="abs f-brand"><span class="brand">BRINDLE<span class="dot"></span></span></div>
  <ul class="abs f-contact">
    <li><span class="ico-c"><svg width="11" height="11" viewBox="0 0 12 12"><path d="M10 12C5 12 0 7 0 2l2-2 3 3-1 2c1 1 2 2 3 3l2-1 3 3z" fill="#fff"/></svg></span>07700 900 418</li>
    <li><span class="ico-c"><svg width="11" height="9" viewBox="0 0 12 9"><rect width="12" height="9" rx="1" fill="#fff"/><path d="M0 1l6 4 6-4" stroke="var(--green)" fill="none"/></svg></span>info@brindle-landscapes.com</li>
  </ul>
  <div class="abs social">
    <span style="background:#1f73e8"></span><span style="background:#1da1f2"></span><span style="background:#e53935"></span>
  </div>

  <div class="f-col" style="left:523px">
    <h5><span>Quick Links</span></h5>
    <a href="#">Home</a><a href="#">About</a><a href="#">Contact</a>
  </div>
  <div class="abs vline" style="left:674px"></div>
  <div class="f-col" style="left:726px">
    <h5 class="y"><span>Sell to Properly</span></h5>
    <a href="#">How it works</a><a href="#">Pricing</a><a href="#">Request Offer</a>
  </div>
  <div class="abs vline" style="left:895px"></div>
  <div class="f-col" style="left:953px">
    <h5><span>Legal</span></h5>
    <a href="#">Terms of use</a><a href="#">Privacy Policy</a>
  </div>
  <div class="abs hline"></div>
  <div class="abs copy">Copyright © 2020 <span>Brindle Landscapes</span></div>
</footer>

</body>
</html>
```